Professional Home Buyer business card needed

I need a pretty straight forward business card designed. We help people that NEED to sell their homes solve problems. We perform all types of Real Estate transactions including flip, wholesale, investment, rental property and multi family. The card will mainly be used to give to prospective Sellers but will also be given to Real Estate Investors as well. It should professional and very easy to read, most clients are older people.

Target Market(s)

Distressed home sellers as well as Real Estate investors

Industry/Entity Type

Real Estate

Contact Information for Business Card

should be a professional layout

Colors
ec1f27
ffffff
000000

Requirements
Must have
• Large logo on back and smaller one on front. should utilize Red, white, and black.
• I am thinking of using a soft touch coating on the card so keep that in mind.
• Contact info should be very easy to read, think older clients.
Nice to have
• I would like to see a design with rounded corners on the card
Should not have
• pictures of homes or other home graphics.

```html
<!DOCTYPE html>
<html lang="en">
<head>
<meta charset="utf-8">
<title>Keystone Home Buyers – Business Card</title>
<link rel="stylesheet" href="https://fonts.googleapis.com/css2?family=Source+Sans+3:wght@400;600;800&display=swap">
<style>
  :root {
    --brand-red: #ec1f27;
    --brand-black: #000000;
    --brand-white: #ffffff;
    --stage: #d9d9d9;
    --ink-soft: #222222;
  }
  * { box-sizing: border-box; margin: 0; padding: 0; }
  html, body { width: 1200px; height: 930px; overflow: hidden; }
  body {
    background: var(--stage);
    font-family: "Source Sans 3", Arial, sans-serif;
    position: relative;
  }
  .card {
    position: absolute;
    width: 580px;
    height: 332px;
    border-radius: 6px;
    overflow: hidden;
    box-shadow: 0 6px 18px rgba(0,0,0,0.25);
  }
  .card--back {
    left: 60px; top: 90px;
    background: var(--brand-black);
    display: flex; align-items: center; justify-content: center;
  }
  .card--front {
    left: 560px; top: 500px;
    background: var(--brand-white);
  }
  .wordmark {
    display: flex; align-items: center; gap: 12px;
    font-weight: 800;
    letter-spacing: 0.04em;
    text-transform: uppercase;
    line-height: 1;
    white-space: nowrap;
  }
  .wordmark__dot {
    width: 18px; height: 18px;
    background: var(--brand-red);
    flex: none;
  }
  .card--back .wordmark { color: var(--brand-white); font-size: 40px; gap: 14px; }
  .card--back .wordmark__dot { width: 30px; height: 30px; }
  .card--front .wordmark {
    position: absolute; left: 34px; top: 140px;
    color: var(--brand-black); font-size: 22px;
  }
  .holder {
    position: absolute; right: 30px; top: 20px;
    text-align: right;
  }
  .holder__name {
    color: var(--brand-red);
    font-size: 26px; font-weight: 600;
    letter-spacing: 0.01em;
    text-transform: uppercase;
    line-height: 1;
  }
  .holder__title {
    color: var(--ink-soft);
    font-size: 15px;
    line-height: 1;
    margin-top: 5px;
  }
  .swoosh { position: absolute; inset: 0; width: 100%; height: 100%; }
  .contact {
    position: absolute; right: 22px; top: 198px;
    list-style: none;
    color: var(--brand-white);
    text-align: right;
    font-size: 15px;
    line-height: 22px;
  }
  .contact li { display: flex; justify-content: flex-end; align-items: center; gap: 8px; }
  .contact svg { width: 12px; height: 12px; flex: none; }
  .contact .spacer { width: 12px; flex: none; }
</style>
</head>
<body>

  <section class="card card--back" aria-label="Card back">
    <div class="wordmark"><span class="wordmark__dot"></span><span>Keystone Home Buyers</span></div>
  </section>

  <section class="card card--front" aria-label="Card front">
    <svg class="swoosh" viewBox="0 0 580 332" aria-hidden="true">
      <path d="M0 318 C130 312 250 294 330 226 C268 300 165 324 40 332 L0 332 Z" fill="var(--brand-red)"/>
      <path d="M580 104 C470 112 405 136 378 194 C345 268 250 314 100 332 L580 332 Z" fill="var(--brand-black)"/>
      <path d="M580 104 C470 112 405 136 378 194 C345 268 250 314 100 332" fill="none" stroke="var(--brand-white)" stroke-width="5"/>
      <path d="M580 84 C458 92 385 118 356 182 C324 254 232 298 70 314" fill="none" stroke="var(--brand-black)" stroke-width="8"/>
    </svg>

    <div class="holder">
      <p class="holder__name">Daniel Brooks</p>
      <p class="holder__title">CEO</p>
    </div>

    <div class="wordmark"><span class="wordmark__dot"></span><span>Keystone Home Buyers</span></div>

    <ul class="contact">
      <li><span>4120 Maple Ridge Drive</span><span class="spacer"></span></li>
      <li><span>Fairview, TX 75069</span><span class="spacer"></span></li>
      <li><span>+1 555 014 2290</span>
        <svg viewBox="0 0 12 12"><path d="M2 1 L4.5 1 L5.5 3.8 L4 4.8 C4.8 6.5 5.6 7.3 7.2 8 L8.2 6.5 L11 7.5 L11 10 C11 10.6 10.6 11 10 11 C5 11 1 7 1 2 C1 1.4 1.4 1 2 1 Z" fill="var(--brand-red)"/></svg></li>
      <li><span>hello@keystonehb.com</span>
        <svg viewBox="0 0 12 12"><rect x="1" y="2.5" width="10" height="7" fill="none" stroke="var(--brand-red)" stroke-width="1.3"/><path d="M1 3 L6 7 L11 3" fill="none" stroke="var(--brand-red)" stroke-width="1.3"/></svg></li>
      <li><span>www.keystonehb.com</span>
        <svg viewBox="0 0 12 12"><circle cx="6" cy="6" r="5" fill="none" stroke="var(--brand-red)" stroke-width="1.2"/><ellipse cx="6" cy="6" rx="2.2" ry="5" fill="none" stroke="var(--brand-red)" stroke-width="1"/><path d="M1 6 H11" stroke="var(--brand-red)" stroke-width="1"/></svg></li>
    </ul>
  </section>

</body>
</html>
```